Dusty Trail Outfitters Home Page

I need a logo and page design for my home page, maybe some background color suggestions to go with it. I want the logo to project "vintage" and "western wear" but not be your typical trite western saddle and gun type thing.
http://www.dustytrailoutfitters.example/store/cart.php
Not looking for page coding just logo and other design elements to lay in over the site's template to make it "pop"
Target Market(s)
My customers are 70/30 men to women.
Industry/Entity Type
Gun
Font styles to use

```html
<!DOCTYPE html>
<html lang="en">
<head>
<meta charset="utf-8">
<title>Dusty Trail Outfitters – Home</title>
<link href="https://fonts.googleapis.com/css2?family=Black+Ops+One&family=Nunito+Sans:wght@400;600;700&display=swap" rel="stylesheet">
<style>
:root{
  --parchment:#c8b78d;
  --parchment-light:#ddd0ac;
  --parchment-dark:#a8956a;
  --ink:#1d1a17;
  --panel:#6a5f4f;
  --panel-text:#f3ede0;
  --accent:#d42b20;
  --promo:#12b6ee;
  --card-frame:#8d8472;
  --footer:#231f1c;
  --footer-text:#a79f93;
}
*{box-sizing:border-box;margin:0;padding:0}
html,body{width:1004px;height:1200px;overflow:hidden}
body{
  font-family:"Nunito Sans",sans-serif;color:var(--ink);position:relative;
  background:
    radial-gradient(ellipse at 30% 20%,var(--parchment-light) 0%,transparent 55%),
    radial-gradient(ellipse at 80% 70%,var(--parchment-light) 0%,transparent 50%),
    linear-gradient(160deg,var(--parchment) 0%,var(--parchment-dark) 100%);
}
.utility-bar{position:absolute;left:454px;top:4px;width:450px;height:34px;background:#6e6456;
  display:flex;align-items:center;justify-content:center;gap:6px;font-size:10px;color:#f0ebe0;letter-spacing:.3px}
.utility-bar span.sep{opacity:.8}
.brand{position:absolute;left:109px;top:50px;display:flex;align-items:center;gap:10px}
.brand .mark{width:20px;height:20px;background:var(--ink)}
.brand .name{font-size:30px;font-weight:700;color:var(--ink);line-height:1.08;width:250px}
.promo-line{position:absolute;left:437px;top:54px;font-size:13px}
.promo-line em{font-style:normal;color:var(--accent)}
.cart{position:absolute;left:770px;top:48px;display:flex;gap:10px;align-items:flex-start}
.cart .label{font-size:13.5px;line-height:1.2}
.cart .label small{font-size:11px;color:var(--accent)}
.field{position:absolute;top:92px;height:25px;background:#fff;border:2px solid #8a8171;
  font-size:10px;color:#555;display:flex;align-items:center;padding:0 8px;justify-content:space-between}
.field.manufacturer{left:511px;width:200px}
.field.search{left:712px;width:184px}
.main-nav{position:absolute;left:109px;top:134px;width:786px;height:44px;background:var(--ink);
  display:flex;justify-content:space-between;align-items:center;padding:0 18px}
.main-nav a{font-family:"Black Ops One",sans-serif;color:#efe9dc;text-decoration:none;font-size:14px;letter-spacing:.5px}
.hero{position:absolute;left:109px;top:184px;width:786px;height:297px;overflow:hidden}
.hero .photo{position:absolute;inset:0;
  background:linear-gradient(90deg,#6b4a32 0%,#8a6a4e 30%,#b9a790 55%,#cfc3b1 75%,#9c8a73 100%)}
.hero h1{position:absolute;right:26px;top:62px;font-family:"Black Ops One",sans-serif;font-weight:400;
  font-size:36px;line-height:1.22;text-align:right;color:#1b1816}
.hero .shop{position:absolute;right:26px;top:164px;width:124px;height:34px;background:var(--accent);
  color:#fff;font-family:"Black Ops One",sans-serif;font-size:17px;display:flex;align-items:center;justify-content:center}
.hero .dots{position:absolute;left:471px;top:272px;display:flex;gap:6px}
.hero .dots i{width:10px;height:10px;border-radius:50%;background:#cfcac2}
.hero .dots i:first-child{background:#fff}
.categories{position:absolute;left:109px;top:508px;width:184px;height:404px;background:var(--panel);padding:14px 17px}
.categories h2{font-size:16px;font-weight:600;color:var(--panel-text);margin-bottom:5px;letter-spacing:.3px}
.categories li{list-style:none;font-size:11px;color:var(--panel-text);line-height:20.9px}
.subscribe{position:absolute;left:109px;top:925px;width:184px;height:131px;background:var(--panel);padding:9px 15px}
.subscribe h2{font-size:16.5px;font-weight:600;color:var(--panel-text);line-height:1.2}
.subscribe .email{margin-top:9px;height:31px;background:#fff;font-size:11px;color:#555;display:flex;align-items:center;padding:0 8px}
.subscribe .btn{margin:9px 0 0 auto;width:89px;height:25px;background:#000;color:#fff;font-size:10px;font-weight:700;display:flex;align-items:center;justify-content:center}
.featured-title{position:absolute;left:322px;top:503px;font-size:20px;font-weight:400;letter-spacing:.3px}
.product{position:absolute;width:179px;height:246px;background:#fff;border:3px solid var(--card-frame);
  text-align:center;padding-top:2px}
.product .image{width:120px;height:134px;margin:0 auto;border-radius:6px}
.product .title{font-size:10.5px;line-height:16.7px;margin-top:6px;padding:0 8px}
.product .price{font-size:15.5px;font-weight:600;margin-top:3px}
.product .add{font-size:11px;color:var(--accent)}
.img-boot{background:linear-gradient(180deg,#7a5a3e,#b04a3a 45%,#33456c 85%,#6a4a33)}
.img-jeans{background:linear-gradient(180deg,#3b5272,#516c92 50%,#3d5675)}
.img-jeans-light{background:linear-gradient(180deg,#5c77a0,#7b96c0 50%,#5a739a)}
.img-tee{background:linear-gradient(180deg,#8ea5c8,#a9bcd8)}
.img-bag{background:linear-gradient(180deg,#8c3a2c,#e0b090 45%,#d6a27c)}
.promo{position:absolute;left:716px;top:808px;width:179px;height:246px;background:var(--promo);
  border:3px solid var(--card-frame);color:#fff;text-align:center;padding:6px 8px}
.promo .up{font-size:13px}
.promo .big{font-size:44px;font-weight:700;color:var(--ink);line-height:1}
.promo .lead{font-size:13px;font-weight:600;line-height:1.3}
.promo .brands{font-size:11px;line-height:15px;margin-top:4px}
.promo .code{font-size:12px;margin-top:8px;line-height:15px}
.promo .code b{font-weight:400;color:var(--ink)}
.promo .terms{font-size:9.5px;margin-top:8px;line-height:13px}
.site-footer{position:absolute;left:0;top:1081px;width:1004px;height:119px;background:var(--footer);color:var(--footer-text)}
.site-footer .links{position:absolute;left:110px;top:27px;display:flex;gap:36px;font-size:11px}
.site-footer .copy{position:absolute;left:110px;top:69px;font-size:10px;line-height:17px}
.site-footer .badge{position:absolute;left:543px;top:28px;width:79px;height:30px;background:#1f5b8f;border-radius:3px}
.site-footer h3{font-size:13px;font-weight:400;color:#d6d0c5}
.pay{position:absolute;left:650px;top:25px}
.pay .cards{display:flex;gap:6px;margin-top:9px}
.pay .cards span{background:#fff;color:var(--ink);font-size:9px;font-weight:600;padding:5px 4px;border-radius:2px}
.social{position:absolute;left:804px;top:25px}
.social .icons{display:flex;gap:6px;margin-top:9px;font-size:9px}
.social .icons span{display:flex;align-items:center;gap:3px;color:#d6d0c5}
.social .icons i{width:12px;height:12px;border-radius:50%;background:#3d7bc4;display:inline-block}
</style>
</head>
<body>
<nav class="utility-bar">
  <span>LOG IN</span><span class="sep">|</span><span>REGISTER</span><span class="sep">|</span><span>MY ACCOUNT</span><span class="sep">|</span><span>SHIPPING &amp; RETURNS</span><span class="sep">|</span><span>FAQ</span><span class="sep">|</span><span>CONTACT US</span>
</nav>

<div class="brand"><span class="mark"></span><span class="name">Dusty Trail Outfitters</span></div>

<p class="promo-line">Like us on Ranchbook and <em>get 5% off</em> your first order.</p>

<div class="cart">
  <svg width="22" height="20" viewBox="0 0 22 20" aria-hidden="true"><path d="M2 7h18l-2 11H4z" fill="#fff"/><path d="M7 7l4-5 4 5" stroke="#fff" stroke-width="2" fill="none"/></svg>
  <div class="label">Shopping Cart<br>$0.00 <small>( Items 0 )</small></div>
</div>

<div class="field manufacturer">MANUFACTURER
  <svg width="12" height="7" viewBox="0 0 12 7" aria-hidden="true"><path d="M0 0h12L6 7z" fill="#444"/></svg></div>
<div class="field search">SEARCH KEYWORD
  <svg width="13" height="13" viewBox="0 0 13 13" aria-hidden="true"><circle cx="5" cy="5" r="4" stroke="#222" stroke-width="1.8" fill="none"/><path d="M8 8l4 4" stroke="#222" stroke-width="2"/></svg></div>

<nav class="main-nav">
  <a>HOME</a><a>ABOUT US</a><a>PRODUCTS</a><a>MEN</a><a>WOMEN</a><a>ACCESSORIES</a><a>SIZING</a><a>SPECIALS</a><a>BLOG</a>
</nav>

<section class="hero">
  <div class="photo" role="img" aria-label="Woman in a cowboy hat and fringed suede jacket beside a horse at sunset"></div>
  <h1>BRAND NEW<br>WESTERN WEAR</h1>
  <div class="shop">SHOP NOW</div>
  <div class="dots"><i></i><i></i><i></i><i></i></div>
</section>

<aside class="categories">
  <h2>CATEGORIES</h2>
  <ul>
    <li>Boots</li><li>Men's Western Wear</li><li>Women's Western Wear</li><li>Brand New Arrivals</li><li>CLEARANCE</li><li>T-Shirts</li><li>Vests</li><li>Accessories</li><li>Jackets</li><li>BELTS</li><li>Hand Bags</li><li>Leather</li><li>On Sale!</li><li>Pants</li><li>Short Sleeves</li><li>Big and Tall</li><li>Jeans</li>
  </ul>
</aside>

<aside class="subscribe">
  <h2>Subscribe to Our Mailing Lists</h2>
  <div class="email">Enter Email</div>
  <div class="btn">SUBSCRIBE</div>
</aside>

<h2 class="featured-title">FEATURED PRODUCTS</h2>

<article class="product" style="left:322px;top:540px">
  <div class="image img-boot" role="img" aria-label="Cowboy boot with American flag stars and stripes shaft"></div>
  <p class="title">Rawhide Ridge Men's AMERICAN FLAG - SNIP TOE BROWN TOE CAP Cowboy Boot</p>
  <p class="price">$219.00</p><p class="add">Add to Cart</p>
</article>
<article class="product" style="left:518px;top:540px">
  <div class="image img-jeans" role="img" aria-label="Dark wash men's bootcut jeans with brown boots"></div>
  <p class="title">Rawhide Ridge Men's AMERICAN FLAG - SNIP TOE BROWN TOE CAP Cowboy Boot</p>
  <p class="price">$219.00</p><p class="add">Add to Cart</p>
</article>
<article class="product" style="left:716px;top:540px">
  <div class="image img-jeans-light" role="img" aria-label="Light wash women's flare jeans"></div>
  <p class="title">Rawhide Ridge Men's AMERICAN FLAG - SNIP TOE BROWN TOE CAP Cowboy Boot</p>
  <p class="price">$219.00</p><p class="add">Add to Cart</p>
</article>
<article class="product" style="left:322px;top:808px">
  <div class="image img-tee" role="img" aria-label="Light blue t-shirt with embroidered western scroll design"></div>
  <p class="title">Rawhide Ridge Men's AMERICAN FLAG - SNIP TOE BROWN TOE CAP Cowboy Boot</p>
  <p class="price">$219.00</p><p class="add">Add to Cart</p>
</article>
<article class="product" style="left:518px;top:808px">
  <div class="image img-bag" role="img" aria-label="Tan suede handbag with star studs and tassels"></div>
  <p class="title">Rawhide Ridge Men's AMERICAN FLAG - SNIP TOE BROWN TOE CAP Cowboy Boot</p>
  <p class="price">$219.00</p><p class="add">Add to Cart</p>
</article>

<aside class="promo">
  <p class="up">Up To</p>
  <p class="big">20%</p>
  <p class="lead">Discount thru June 15th<br>on</p>
  <p class="brands">Prairie Slim, Rawhide Ridge, Mesa Hat Co., Juniper Ranch, Growl, Ryder Mitchell Mens and Ryder Mitchell Womens</p>
  <p class="code">Use coupon code:<br><b>trail20</b></p>
  <p class="terms">Applies to order totals of<br>$60 or more</p>
</aside>

<footer class="site-footer">
  <div class="links"><span>About Us</span><span>Contact Us</span><span>Shipping &amp; Returns</span><span>Privacy</span></div>
  <p class="copy">Copyright © 2014. Dusty Trail Outfitters.<br>All Right Reserved</p>
  <div class="badge" aria-label="Accreditation badge"></div>
  <div class="pay"><h3>Secure Payment:</h3>
    <div class="cards"><span>PayPouch</span><span>Carduna</span><span>Maplecard</span></div></div>
  <div class="social"><h3>Connect Us</h3>
    <div class="icons"><span><i></i>Ranchbook</span><span><i></i>Chatterly</span><span><i></i>Circlehub</span></div></div>
</footer>
</body>
</html>
```